Business Card for Restaurant Vendal

This project consist of creating 2 design for business card of restaurant named Vendal.

The attached specs below are 'ONLY SUGGESTION' if you have others ideas. You are welcome to post it.

1) Restaurant Card

Adresse:
2784 Côte du Pinard Vert
Montréal (Qc) H4K 3T8

Website:
www.ven-dal.ca

Phone:
438-719-2046

2) Employee Card

Name: Lorna Pik
Title: Owner

Address:
2784 Côte du Pinard Vert
Montréal (Qc) H4K 3T8

Email:lorna@ven-dal.ca
Phone Number:438-719-2046
Cellphone Number:514-830-4162

 The attached specs are 'ONLY SUGGESTION' if you have others ideas.  You are welcome to post it.

Industry/Entity Type

Restaurant

Requirements
Must have
• UV Card Spot

To print Spot UV business cards you would have to submit 2 files for each side. The first file "base" would be your regular design file as it would have been in any other case. The 2nd file "UV mask" is a black/white file. The BLACK color will indicate the areas that will be covered with the UV high gloss finish. To upload the files, please combine front design and front mask file in one P
Nice to have
• 1) The font of the logo should be ink effect
2) black background with wallpaper effect
3) The specs below are 'ONLY SUGGESTION' if you have others ideas. You are welcome to post it.

```html
<!DOCTYPE html>
<html lang="fr">
<head>
<meta charset="utf-8">
<title>Vendal – Cartes d'affaires</title>
<link rel="stylesheet" href="https://fonts.googleapis.com/css2?family=Yuji+Syuku&family=Noto+Sans+JP:wght@500;700&display=swap">
<style>
  :root {
    --backdrop: #2e2019;
    --card: #ffffff;
    --card-shade: #e4e4e4;
    --ink: #1c1c1c;
    --ink-soft: #2a2a2a;
  }
  html, body {
    margin: 0;
    padding: 0;
    width: 1200px;
    height: 900px;
    overflow: hidden;
    background: var(--backdrop);
  }
  .canvas {
    position: relative;
    width: 1200px;
    height: 900px;
  }
  .card {
    position: absolute;
    width: 586px;
    height: 337px;
    border-radius: 18px;
    background: radial-gradient(ellipse at 55% 40%, var(--card) 55%, var(--card-shade) 100%);
    overflow: hidden;
  }
  .card--back { left: 147px; top: 85px; }
  .card--front { left: 514px; top: 466px; }

  .brand {
    position: absolute;
    display: flex;
    align-items: center;
    gap: 14px;
    font-family: "Noto Sans JP", sans-serif;
    font-weight: 700;
    color: var(--ink);
    letter-spacing: 0.02em;
  }
  .brand__dot {
    flex: none;
    border-radius: 50%;
    background: var(--ink);
  }
  .card--back .brand {
    left: 54px;
    top: 104px;
    font-size: 46px;
  }
  .card--back .brand__dot { width: 92px; height: 92px; }

  .izakaya {
    position: absolute;
    left: 78px;
    top: 92px;
    margin: 0;
    font-family: "Yuji Syuku", serif;
    font-size: 48px;
    font-weight: 400;
    letter-spacing: 0.12em;
    color: var(--ink-soft);
  }
  .card--front .brand {
    right: 68px;
    top: 178px;
    font-size: 54px;
    gap: 10px;
  }
  .card--front .brand__dot { width: 30px; height: 30px; }
  .tagline {
    position: absolute;
    right: 62px;
    top: 264px;
    margin: 0;
    font-family: "Noto Sans JP", sans-serif;
    font-weight: 500;
    font-size: 10px;
    color: var(--ink);
    letter-spacing: 0.02em;
  }
</style>
</head>
<body>
  <main class="canvas">
    <section class="card card--back" aria-label="Verso de la carte">
      <div class="brand">
        <span class="brand__dot" aria-hidden="true"></span>
        <span class="brand__name">Vendal</span>
      </div>
    </section>

    <section class="card card--front" aria-label="Recto de la carte">
      <h2 class="izakaya" lang="ja">居酒屋</h2>
      <div class="brand">
        <span class="brand__name">Vendal</span>
        <span class="brand__dot" aria-hidden="true"></span>
      </div>
      <p class="tagline">Resto-Bar Japonais · Izakaya · <span lang="ja">居酒屋</span></p>
    </section>
  </main>
</body>
</html>
```